Tending Our Garden eBook Cover Design

I want to deisgn a cover for my eBook (FRONT COVER) and the title is:

What I Grew From a Single Spark. And Why It Matters
By KT Dorran

TITLE CHANGED TO: UNDER THE WILLOW TREE; WHERE I FOUND MY QUIET STRENGTH AND WHERE YOU MIGHT TOO

The color palette is attached. Along with some photos options of me. Along with the ebook in WORD Document. My website is www.KTDorranLive.example. You can use a different color palette if you think it is best

Target Market(s)

women who look to build a personal brand

Industry/Entity Type

health and wellness

Requirements
Must have
• the title
Nice to have
• use my picture on the cover; but that is optional
Should not have
• any men

```html
<!DOCTYPE html>
<html lang="en">
<head>
<meta charset="utf-8">
<title>Under the Willow Tree — KT Dorran</title>
<link rel="stylesheet" href="https://fonts.googleapis.com/css2?family=Anton&family=Montserrat:wght@900&display=swap">
<style>
  :root {
    --cover-yellow: #ffe500;
    --ink-black: #141414;
    --accent-red: #e2263b;
    --paper-white: #ffffff;
    --figure-blue: #2298f2;
    --figure-red: #d52f30;
  }
  html, body {
    margin: 0;
    padding: 0;
    width: 800px;
    height: 1200px;
    overflow: hidden;
    background: var(--cover-yellow);
  }
  .cover {
    position: relative;
    width: 800px;
    height: 1200px;
    background: var(--cover-yellow);
    overflow: hidden;
  }
  .cover-title {
    position: absolute;
    left: 0;
    top: 0;
    width: 800px;
    height: 770px;
  }
  .cover-title text {
    font-family: "Anton", "Oswald", sans-serif;
  }
  .title-dark { fill: var(--ink-black); }
  .title-accent { fill: var(--accent-red); }
  .cover-figure {
    position: absolute;
    left: 230px;
    top: 765px;
    width: 338px;
    height: 352px;
    border-radius: 170px 170px 14px 14px;
    background: linear-gradient(180deg, var(--figure-blue) 0%, var(--figure-blue) 45%, var(--figure-red) 70%, var(--figure-red) 100%);
  }
  .author-band {
    position: absolute;
    left: 0;
    bottom: 0;
    width: 800px;
    height: 83px;
    background: var(--accent-red);
    display: flex;
    align-items: center;
    justify-content: center;
  }
  .author-name {
    margin: 0;
    font-family: "Montserrat", "Arial Black", sans-serif;
    font-weight: 900;
    font-size: 46px;
    letter-spacing: 2px;
    color: var(--paper-white);
    text-transform: uppercase;
    line-height: 1;
  }
</style>
</head>
<body>
  <main class="cover">
    <svg class="cover-title" viewBox="0 0 800 770" role="heading" aria-level="1" aria-label="Under the Willow Tree; Where I Found My Quiet Strength and Where You Might Too">
      <text class="title-dark" x="69" y="223" font-size="176" textLength="664" lengthAdjust="spacingAndGlyphs">UNDER THE</text>
      <text class="title-accent" x="67" y="351" font-size="113" textLength="666" lengthAdjust="spacingAndGlyphs">WILLOW TREE</text>
      <text class="title-dark" x="74" y="493" font-size="130" textLength="651" lengthAdjust="spacingAndGlyphs">WHERE I FOUND MY</text>
      <text class="title-dark" x="74" y="648" font-size="130" textLength="651" lengthAdjust="spacingAndGlyphs">QUIET STRENGTH</text>
      <text class="title-accent" x="85" y="750" font-size="85" textLength="627" lengthAdjust="spacingAndGlyphs">AND WHERE YOU MIGHT TOO</text>
    </svg>

    <div class="cover-figure" role="img" aria-label="Illustration of a calm winged figure with blue hair wearing a red top with a coin emblem"></div>

    <footer class="author-band">
      <p class="author-name">KT Dorran</p>
    </footer>
  </main>
</body>
</html>
```